cartNest - a stylish trolley for apartments

We neede a simple website to sell our Trolley, for apartment use.
The colour theme is red, blask & white. Our logo is attached and this needs to be on the Home page.
The website only needs a Home Page plus 4 other pges.
In the attachment you will find a site map.

You can check out the following two sites to see what I like:
www.plinthgallery.example/design-showcase-inspiration/minimalist-portfolio-website/
www.brightquarry.example/inspiration/40-beautiful-web-design-portfolios/ in this site especially
Dario Menezes
K B Forge
Nine 17 Studio
Oliver Marsh

And especially Lamp - I ike the simpicity of the site esp as we are only selling one product

Target Market(s)

Apartment dwellers

Industry/Entity Type

Apartment

Requirements
Must have
• This website must have 4 pages.
We need Corvo, Ledgerline and Quidly portals.
Order Form for Trolley
Payment form.

```html
<!DOCTYPE html>
<html lang="en">
<head>
<meta charset="utf-8">
<title>cartNest – a stylish trolley for apartments</title>
<link rel="stylesheet" href="https://fonts.googleapis.com/css2?family=Mulish:wght@600;700&family=Arimo:wght@400;700&family=Tinos&display=swap">
<style>
:root{
  --ink:#111;
  --white:#fff;
  --red:#c8161d;
  --gold:#f4c94c;
  --text:#555;
  --muted:#777;
  --panel-line:#9a9a9a;
  --band:#efefef;
  --thumb-border:#c9c9c9;
}
*{box-sizing:border-box;margin:0;padding:0}
html,body{width:1200px;height:1113px;overflow:hidden;background:var(--white)}
body{position:relative;font-family:"Mulish",Arial,sans-serif;color:var(--text)}
a{color:inherit;text-decoration:none}

.topbar{position:absolute;left:0;top:0;width:1200px;height:48px;
  background:linear-gradient(#2b2b2b,#0d0d0d);border-bottom:1px solid #000}
.nav{position:absolute;top:11px;left:0;font-size:19px;font-weight:700;color:var(--white)}
.nav a{position:absolute;white-space:nowrap}
.brand-dot{display:inline-block;width:7px;height:7px;background:var(--red);border-radius:50%;margin-right:6px;vertical-align:middle}
.cartlinks{position:absolute;left:893px;top:9px;display:flex;align-items:center;gap:7px;color:var(--white);font-size:14px;font-weight:700;font-family:"Arimo",sans-serif}
.cartlinks svg{width:36px;height:30px}

.slider{position:absolute;left:106px;top:64px;width:982px;height:450px}
.slider svg{position:absolute;left:0;top:0}
.caption{position:absolute;left:42px;top:365px;color:var(--white)}
.caption h2{font-size:26px;color:var(--gold);font-weight:700;letter-spacing:.2px;line-height:30px}
.caption p{font-size:16px;font-weight:700;margin-top:4px;line-height:20px}
.pager{position:absolute;left:829px;top:402px;display:flex;gap:10px;font-family:"Tinos",serif;font-size:18px;color:var(--white)}
.pager .on{color:var(--gold);font-weight:700}

.panel{position:absolute;top:561px;width:312px;height:181px;border:1px solid var(--panel-line);border-radius:4px;
  background:linear-gradient(#fff 55%,#ececec);overflow:hidden}
.panel h3{height:35px;background:linear-gradient(#2c2c2c,#000);border-bottom:3px solid var(--gold);
  color:var(--white);font-size:21px;font-weight:700;line-height:30px;padding:0 0 0 19px}
.panel-trolley{left:116px}
.panel-contact{left:441px}
.panel-pay{left:766px}
.review{position:relative;height:61px;padding:15px 6px 0 64px;font-family:"Arimo",sans-serif;font-size:10.5px;line-height:13px;color:var(--muted);font-weight:700}
.avatar{position:absolute;left:12px;top:8px;width:47px;height:48px;background:linear-gradient(#c9a98d,#8a6a55);border:1px solid #bbb}
.avatar.alt{background:linear-gradient(#e9ecef,#8b99a6)}
.review .more{position:absolute;right:7px;bottom:1px;font-size:9.5px;color:#222}
.viewmore{font-family:"Arimo",sans-serif;font-size:9.5px;font-weight:700;color:#222;padding:9px 0 0 16px}
.line{font-family:"Arimo",sans-serif;font-weight:700;font-size:15px;color:#666;position:absolute;left:15px}
.line b{color:#111}
.paycards{position:absolute;left:19px;top:127px;display:flex;gap:6px}
.paycards span{border:1px solid #999;background:#fafafa;padding:2px 6px;font-family:"Arimo",sans-serif;font-size:12px;font-weight:700;color:#444}

.about-band{position:absolute;left:0;top:792px;width:1200px;height:241px;background:var(--band)}
.about{position:absolute;left:117px;top:813px;width:455px}
.about h4{font-family:"Tinos",serif;font-weight:400;font-size:19px;color:#555}
.about h4 b{font-family:"Arimo",sans-serif;color:var(--ink)}
.about h4 .red{color:var(--red)}
.about p{margin-top:10px;font-family:"Arimo",sans-serif;font-weight:700;font-size:13px;line-height:20px;color:#666}
.btn{display:inline-block;margin-top:14px;border:1px solid #999;border-radius:4px;background:linear-gradient(#fff,#e4e4e4);padding:6px 4px;font-size:12.5px;color:#222;font-family:"Arimo",sans-serif}
.gallery{position:absolute;left:647px;top:812px}
.gallery h4{font-size:19px;font-weight:700;color:#666}
.thumbs{display:flex;gap:7px;margin-top:8px}
.thumb{width:103px;height:100px;border:3px solid var(--thumb-border)}
.g-arrow{position:absolute;top:140px;width:28px;height:28px}

.footer{position:absolute;left:0;top:1033px;width:1200px;height:80px;background:linear-gradient(#2a2a2a,#0b0b0b);border-top:3px solid #cfcfcf;color:var(--white)}
.copy{position:absolute;left:116px;top:31px;font-size:13px;font-family:"Arimo",sans-serif;font-weight:700}
.copy .red{color:var(--red)}
.footnav{position:absolute;top:28px;left:0;font-size:16px;font-weight:700}
.footnav a{position:absolute;white-space:nowrap}
</style>
</head>
<body>

<header class="topbar">
  <nav class="nav">
    <a style="left:117px"><span class="brand-dot"></span>cartNest</a>
    <a style="left:262px">Gallery</a>
    <a style="left:374px">Contact us</a>
    <a style="left:527px">Shopping cart payment</a>
  </nav>
  <div class="cartlinks">
    <svg viewBox="0 0 36 30" aria-hidden="true"><path d="M1 3h6l4 17h19l4-12H9" fill="none" stroke="#ddd" stroke-width="2"/><circle cx="13" cy="25" r="2.5" fill="#ddd"/><circle cx="27" cy="25" r="2.5" fill="#ddd"/></svg>
    <a>My cart</a><span>|</span><a>Chek out</a>
  </div>
</header>

<section class="slider">
  <svg width="982" height="450" viewBox="0 0 982 450">
    <defs>
      <filter id="shade" x="-5%" y="-5%" width="110%" height="115%"><feDropShadow dx="0" dy="4" stdDeviation="4" flood-opacity=".35"/></filter>
      <linearGradient id="scene" x1="0" y1="0" x2="1" y2="0">
        <stop offset="0" stop-color="#080808"/><stop offset=".33" stop-color="#1a1a1a"/>
        <stop offset=".34" stop-color="#c9c2b8"/><stop offset=".6" stop-color="#b7463f"/>
        <stop offset=".75" stop-color="#d9cfc2"/><stop offset="1" stop-color="#a8927a"/>
      </linearGradient>
      <linearGradient id="cap" x1="0" y1="0" x2="0" y2="1"><stop offset="0" stop-color="#000" stop-opacity=".35"/><stop offset="1" stop-color="#000" stop-opacity=".75"/></linearGradient>
    </defs>
    <path d="M10 70 Q491 -50 972 70 V434 H10 Z" fill="#fff" filter="url(#shade)"/>
    <path d="M20 80 Q491 -30 958 80 V424 H20 Z" fill="url(#scene)" role="img" aria-label="Photo of a hotel luggage trolley loaded with red suitcases beside a staircase, next to a black wall sign"/>
    <rect x="20" y="362" width="500" height="62" fill="url(#cap)"/>
    <path d="M790 400 H958 V424 H775 Z" fill="#222"/>
    <circle cx="14" cy="252" r="21" fill="#fff"/><path d="M19 244 v16 l-11 -8z" fill="#111"/>
    <circle cx="968" cy="252" r="21" fill="#fff"/><path d="M955 244 v16 l11 -8z" fill="#111"/>
  </svg>
  <div class="caption">
    <h2>Lorem ipsum dolor</h2>
    <p>Lorem ipsum dolor sit amet, consectetur adipiscing elit.</p>
  </div>
  <div class="pager"><span>1</span><span>2</span><span class="on">3</span><span>4</span><span>5</span></div>
</section>

<article class="panel panel-trolley">
  <h3>cartNest</h3>
  <div class="review"><div class="avatar" role="img" aria-label="Customer portrait"></div>IT LOOKS GREAT! Designed along the lines of the familiar hotel “birdcage” luggage trolley,<a class="more">&gt;&gt; Read More</a></div>
  <div class="review"><div class="avatar alt" role="img" aria-label="Customer portrait"></div>IT LOOKS GREAT! Designed along the lines of the familiar hotel “birdcage” luggage trolley,<a class="more">&gt;&gt; Read More</a></div>
  <div class="viewmore">▾ View More</div>
</article>

<article class="panel panel-contact">
  <h3>Contact us</h3>
  <p class="line" style="top:52px">Phone : 5550 2187 430</p>
  <p class="line" style="top:88px">Email : <b>hello@cartnest.example</b></p>
  <p class="line" style="top:130px;left:13px">cartNest Contact detail:</p>
</article>

<article class="panel panel-pay">
  <h3>Shopping cart payment</h3>
  <p class="line" style="top:52px;left:19px">Order form ▾</p>
  <p class="line" style="top:88px;left:18px">Payment from Incl</p>
  <div class="paycards"><span>Corvo</span><span>Ledgerline</span><span>Quidly</span></div>
</article>

<div class="about-band"></div>
<section class="about">
  <h4>About <b><span class="red">cartNest</span></b> :</h4>
  <p>cartNest originated from our personal experience of apartment living, and the hassle of taking shopping, luggage, etc, from your car to your apartment. We have sourced trolleys from all over the place,</p>
  <a class="btn">Read More</a>
</section>
<section class="gallery">
  <h4>Gallery</h4>
  <div class="thumbs">
    <div class="thumb" style="background:linear-gradient(#7a2a25,#c9b9a8)" role="img" aria-label="Close-up of trolley wheels"></div>
    <div class="thumb" style="background:linear-gradient(#9a8f83,#5e524a)" role="img" aria-label="Trolley with suitcases in a lift"></div>
    <div class="thumb" style="background:linear-gradient(#6c6a66,#b4403a)" role="img" aria-label="Person loading a trolley from a car"></div>
    <div class="thumb" style="background:linear-gradient(#bcc6cc,#8e9aa2)" role="img" aria-label="Empty chrome trolley"></div>
  </div>
  <svg class="g-arrow" style="left:0" viewBox="0 0 28 28" aria-hidden="true"><circle cx="14" cy="14" r="13" fill="#f6f6f6" stroke="#888"/><path d="M17 8v12l-9-6z" fill="#333"/></svg>
  <svg class="g-arrow" style="left:403px" viewBox="0 0 28 28" aria-hidden="true"><circle cx="14" cy="14" r="13" fill="#f6f6f6" stroke="#888"/><path d="M11 8v12l9-6z" fill="#333"/></svg>
</section>

<footer class="footer">
  <p class="copy">© 2012 All Rights Reserved <span class="red">cartNest</span></p>
  <nav class="footnav">
    <a style="left:536px"><span class="brand-dot"></span>cartNest</a>
    <a style="left:656px">Gallery</a>
    <a style="left:749px">Contact us</a>
    <a style="left:876px">Shopping cart payment</a>
  </nav>
</footer>

</body>
</html>
```